Contemporary Elegant Business Card Design for an International Trade Company in the Wine Industry

We need a new business card design for an international trade company in the wine and winemaking industry. The overall feel of the card should be contemporary, upscale, luxurious and elegant. It should communicate confidence and professionalism. The colors should complementary to our logo design (burgundy, gold, and black).
Inspiration: rich velvet tapestry
The card should include the following information:
Business: Brovenna Trading/Shipping, LLC.
Name: Marcus T. Hollenbrand
Title: CEO
Email: mark@brovennatrading.example
Phone: 555-294-6172
www.brovennatrading.example
Updates
Project Deadline Extended
Reason: We'd like the designers that we requested some additional designs from to still submit designs. Thank you!
Industry/Entity Type
Business
Contact Information for Business Card
Title: CEO
Phone: 555-294-6172
www.brovennatrading.example
Look and feel

```html
<!DOCTYPE html>
<html lang="en">
<head>
<meta charset="utf-8">
<title>Brovenna Trading/Shipping — Business Card</title>
<link rel="stylesheet" href="https://fonts.googleapis.com/css2?family=Cinzel:wght@400;700&family=Sorts+Mill+Goudy&display=swap">
<style>
  :root {
    --backdrop: #d9d9d9;
    --gold-light: #e2b85c;
    --gold: #c9942f;
    --gold-deep: #a8731f;
    --rust-light: #b56d2a;
    --rust: #94501c;
    --rust-deep: #6e3612;
    --burgundy: #5c1016;
    --burgundy-deep: #3f080c;
    --text-gold: #d9a74a;
    --text-gold-bright: #e8bd62;
  }
  * { box-sizing: border-box; margin: 0; padding: 0; }
  html, body {
    width: 1200px; height: 926px; overflow: hidden;
    background: var(--backdrop);
  }
  .sheet {
    width: 1200px; height: 926px;
    display: flex; flex-direction: column; align-items: center; justify-content: center;
    gap: 40px;
  }
  .card {
    position: relative;
    width: 700px; height: 400px;
    overflow: hidden;
    box-shadow: 0 6px 18px rgba(0,0,0,.25);
  }

  /* Front: contact side */
  .card--front {
    background:
      radial-gradient(ellipse at 85% 10%, rgba(90,50,10,.35), transparent 45%),
      radial-gradient(ellipse at 10% 90%, rgba(120,70,15,.3), transparent 50%),
      linear-gradient(135deg, var(--gold) 0%, var(--gold-light) 45%, var(--gold) 100%);
  }
  .card__edge-strip {
    position: absolute; left: 0; top: 90px; width: 14px; height: 230px;
    background: var(--burgundy);
  }
  .brand {
    position: absolute;
    display: flex; align-items: center; gap: 10px;
    font-family: "Sorts Mill Goudy", serif;
    color: var(--burgundy-deep);
  }
  .brand__mark {
    width: 14px; height: 14px; background: var(--burgundy-deep);
  }
  .brand--front {
    left: 40px; top: 186px; font-size: 30px;
  }
  .contact-panel {
    position: absolute; left: 268px; top: 82px; right: 0; height: 240px;
    background:
      radial-gradient(ellipse at 80% 20%, rgba(0,0,0,.25), transparent 60%),
      linear-gradient(160deg, var(--burgundy) 0%, var(--burgundy-deep) 100%);
    padding: 20px 24px 0 28px;
    color: var(--text-gold);
    font-family: "Sorts Mill Goudy", serif;
  }
  .contact-panel__company {
    font-size: 22px; color: var(--gold-deep); margin-bottom: 18px;
    white-space: nowrap;
  }
  .contact-panel__person {
    font-family: "Cinzel", serif; font-weight: 700;
    font-size: 19px; color: var(--text-gold-bright); margin-bottom: 6px;
    white-space: nowrap;
  }
  .contact-panel__title { font-weight: 400; font-size: 17px; }
  .contact-panel__line {
    font-size: 21px; line-height: 1.3; white-space: nowrap;
  }

  /* Back: brand side */
  .card--back {
    background:
      linear-gradient(120deg, var(--rust-deep) 0%, var(--rust) 40%, var(--rust-light) 100%);
  }
  .card__shade {
    position: absolute; inset: 0;
    background: linear-gradient(65deg, rgba(0,0,0,0) 35%, rgba(0,0,0,.12) 35%, rgba(0,0,0,.12) 100%);
  }
  .card__map-field {
    position: absolute; right: 0; top: 0; width: 45%; height: 100%;
    background: radial-gradient(ellipse at 50% 45%, rgba(200,130,60,.45), transparent 70%);
  }
  .brand--back {
    left: 0; right: 0; top: 0; bottom: 0;
    justify-content: center;
    font-size: 44px; color: var(--text-gold-bright);
  }
  .brand--back .brand__mark { width: 18px; height: 18px; background: var(--text-gold-bright); }
</style>
</head>
<body>
<main class="sheet">

  <section class="card card--front" aria-label="Business card, contact side">
    <div class="card__edge-strip"></div>
    <div class="brand brand--front"><span class="brand__mark"></span>Brovenna</div>
    <div class="contact-panel">
      <p class="contact-panel__company">Brovenna Trading/Shipping, LLC.</p>
      <p class="contact-panel__person">Marcus T. Hollenbrand <span class="contact-panel__title">- CEO</span></p>
      <p class="contact-panel__line">mark@brovennatrading.example</p>
      <p class="contact-panel__line">555-294-6172</p>
      <p class="contact-panel__line">www.brovennatrading.example</p>
    </div>
  </section>

  <section class="card card--back" aria-label="Business card, brand side">
    <div class="card__shade"></div>
    <div class="card__map-field" role="img" aria-label="Faint world map texture"></div>
    <div class="brand brand--back"><span class="brand__mark"></span>Brovenna</div>
  </section>

</main>
</body>
</html>
```